Need help revamping our cards for Prescription Assistance Program

Would like to go with something in a Black Theme that grabs attention and looks official. I have included some of our previous designs. The Blue/White version is our most current version so would like to follow its format regarding the information. Perhaps, one side white, the other black(might be different/catchy)
Cards are not to have pharmacy logos. Would like to have the ability to update cards with new member IDs. Would also desire a continued relationship with the designer to update and/or modify for regional needs.
Thank you

needs information stacked on the right side for easy viewing whilst flipping through a stack of competitor's cards

please include VELMAR Code

Target Market(s)

pharmacies(pharmacist, techs), general public

Requirements
Must have
• eye catching, official looking, information aragned in an easy to view format, desired to standout if in an stack of 20 other cards
Should not have
• pharmacy logos

```html
<!DOCTYPE html>
<html lang="en">
<head>
<meta charset="utf-8">
<title>MedPass Discount Prescription Drug Card</title>
<link href="https://fonts.googleapis.com/css2?family=Open+Sans:wght@400;600;700;800&display=swap" rel="stylesheet">
<style>
  :root {
    --bg: #2a2d31;
    --card-black: #0c0c0d;
    --card-white: #ffffff;
    --grey-band: #5a5a5c;
    --brand-blue: #3a4a8c;
    --accent-red: #c8262e;
    --text-light: #f2f2f2;
    --text-muted: #cfcfcf;
  }
  * { box-sizing: border-box; margin: 0; padding: 0; }
  html, body { width: 1200px; height: 900px; overflow: hidden; }
  body {
    background: var(--bg);
    font-family: "Open Sans", Arial, sans-serif;
    display: flex;
    align-items: center;
    justify-content: center;
    gap: 40px;
  }
  .card {
    position: relative;
    width: 560px;
    height: 320px;
    border-radius: 26px;
    overflow: hidden;
  }
  .card-art { position: absolute; inset: 0; width: 100%; height: 100%; }

  /* Front */
  .front .brand-block {
    position: absolute;
    left: 34px;
    top: 92px;
    width: 300px;
  }
  .front .tagline {
    font-size: 17px;
    font-weight: 700;
    letter-spacing: 0.5px;
    color: var(--accent-red);
    border-bottom: 1px solid #bbb;
    padding-bottom: 4px;
    margin-bottom: 6px;
  }
  .front .brand-name {
    font-size: 74px;
    font-weight: 800;
    line-height: 1;
    color: var(--brand-blue);
    letter-spacing: -2px;
  }
  .front .attention {
    position: absolute;
    left: 402px;
    right: 10px;
    top: 44px;
    color: var(--text-light);
  }
  .front .attention-title {
    font-size: 11px;
    letter-spacing: 0;
  }
  .front .attention-note {
    font-size: 8.5px;
  }

  .attention-title {
    font-size: 15px;
    font-weight: 700;
    letter-spacing: 0.3px;
    padding-bottom: 3px;
    border-bottom: 2px solid var(--accent-red);
    display: inline-block;
    margin-bottom: 4px;
    white-space: nowrap;
  }
  .attention-note {
    font-size: 9.5px;
    line-height: 1.35;
    color: var(--text-muted);
  }

  /* Back */
  .back { background: var(--card-black); color: var(--text-light); }
  .back .brand-block {
    position: absolute;
    left: 0; right: 0;
    top: 22px;
    text-align: center;
  }
  .back .brand-name {
    font-size: 46px;
    font-weight: 800;
    line-height: 1;
    color: var(--brand-blue);
    letter-spacing: -1px;
  }
  .back .card-type {
    display: inline-block;
    margin-top: 4px;
    font-size: 13px;
    padding-bottom: 2px;
    border-bottom: 1px solid var(--accent-red);
  }
  .benefits {
    position: absolute;
    left: 40px; right: 40px;
    top: 108px;
    list-style: none;
    display: grid;
    grid-template-columns: 1fr 1fr;
    gap: 5px 16px;
    font-size: 11px;
  }
  .benefits li::before {
    content: "";
    display: inline-block;
    width: 6px; height: 6px;
    border-radius: 50%;
    background: var(--accent-red);
    margin-right: 6px;
    vertical-align: middle;
  }
  .member-fields {
    position: absolute;
    left: 40px; right: 40px;
    top: 168px;
    display: grid;
    grid-template-columns: 1fr 1fr;
    gap: 12px 24px;
    font-size: 17px;
    font-weight: 700;
  }
  .field { display: flex; gap: 22px; }
  .field dt { width: 50px; }
  .back .attention {
    position: absolute;
    left: 40px;
    bottom: 22px;
    width: 240px;
  }
</style>
</head>
<body>

  <section class="card front" aria-label="Card front">
    <svg class="card-art" viewBox="0 0 560 320" aria-hidden="true">
      <defs>
        <linearGradient id="sweep" x1="0" y1="0" x2="1" y2="1">
          <stop offset="0" stop-color="#4a4a4c"/>
          <stop offset="1" stop-color="#111"/>
        </linearGradient>
      </defs>
      <rect width="560" height="320" fill="#0c0c0d"/>
      <path d="M0 0 H300 C360 60 390 170 360 320 H0 Z" fill="#ffffff"/>
      <path d="M300 0 H330 C400 80 420 200 380 320 H360 C390 170 360 60 300 0 Z" fill="url(#sweep)"/>
      <path d="M380 320 C420 230 470 210 560 220 V320 Z" fill="#1c1c1e"/>
    </svg>
    <div class="brand-block">
      <p class="tagline">PRESCRIPTION AT A DISCOUNT</p>
      <p class="brand-name">MedPass</p>
    </div>
    <div class="attention">
      <p class="attention-title">ATTENTION PHARMACIST</p>
      <p class="attention-note">If you are unable to process a prescription through the program, please call (800)-555-0142</p>
    </div>
  </section>

  <section class="card back" aria-label="Card back">
    <svg class="card-art" viewBox="0 0 560 320" aria-hidden="true">
      <defs>
        <linearGradient id="band" x1="0" y1="0" x2="1" y2="0">
          <stop offset="0" stop-color="#0c0c0d"/>
          <stop offset="0.5" stop-color="#5a5a5c"/>
          <stop offset="1" stop-color="#0c0c0d"/>
        </linearGradient>
      </defs>
      <rect x="0" y="98" width="560" height="56" fill="url(#band)"/>
      <line x1="30" y1="250" x2="530" y2="250" stroke="#3a3a3c" stroke-width="1"/>
    </svg>
    <div class="brand-block">
      <p class="brand-name">MedPass</p>
      <p class="card-type">Discount Prescription Drug Card</p>
    </div>
    <ul class="benefits">
      <li>100% HIPAA Compliant</li>
      <li>Up to 90% Instant Saving</li>
      <li>Largest saving on FAST MOVERS</li>
      <li>Always defaults to LOWER of PRICING</li>
    </ul>
    <dl class="member-fields">
      <div class="field"><dt>BIN:</dt><dd>000000</dd></div>
      <div class="field"><dt>PCN:</dt><dd>AAAA0</dd></div>
      <div class="field"><dt>GRP:</dt><dd>MEDPASS</dd></div>
      <div class="field"><dt>ID:</dt><dd>MED000</dd></div>
    </dl>
    <div class="attention">
      <p class="attention-title">ATTENTION PHARMACIST</p>
      <p class="attention-note">If you are unable to process a prescription through the program, please call (800)-555-0142</p>
    </div>
  </section>

</body>
</html>
```